Dr K.L. Fenwick, Consultant General Surgeon

Modern minimalistic look [shades of blue should be included]
I would like an interactive website which gives information about
1. Home page: office location
Medical Partners
📞(876) 555-0192-7
📱(876) 555-0147
📍42 Marigold Crescent, Kingston 10

VelaMedix
1-876-555-0163 / 1-876-555-0178 / 1-876-555-0129
📍37 North Cedar Grove RD, Kingston, Jamaica (Upstairs Brisa Linwood)
Info@velamedix.example

Beacon Care Medical Suites
📞(876) 555-0184
📱(876) 555-0136
📍Shop 22-23, Palm Crest Shopping Mall, Portmore

Corwell Medical Centre
📞 (876) 555-0151
📍 9 Pellowin Street , May Pen
The office logos will be attached
Booking details on this page or 2nd page with procedures

2. My surgical services . - I will attach a business card with the information for this section - do not upload the actual business card on the site

3. Allow the booking of appointments at any of the offices
4. A section where short explainer videos will be uploaded (this section is titled "Surgery in 3D"- I will upload an example below
5. A section- which shows videos of procedures. This section is titled "Surgical procedures" - I will upload one below
these videos will similar the same as the ones on my Instagram account
Link: https://www.instagram.com/dr_klfenwick?igsh=QmVyZXhhbXBsZQ&utm_source=qr

6. Gallery- section with pictures from interviews/ presentations/conferences etc

Each section should be on a different page.
The clearly defined sections can be represented from a HOME PAGE or drop-down menu
SIMILAR websites:
Modern professional design style (fonts and layout)- https://brightscalpelstudio.example
others -- this best captures the style I'm looking for. I prefer if the page is not crowded
https://velamedix.example
layered effect -- https://quillbankclinic.example/general-surgeon/
https://drpetrahalvik.example

I have updated the brief

Target Market(s)

Patients who require general surgical care

Coding

Coded - Design and coding required

Number of Pages Required

5+ page

Requirements
Must have
• Each section should be on a different page.

```html
<!DOCTYPE html>
<html lang="en">
<head>
<meta charset="utf-8">
<title>Dr K.L. Fenwick — Consultant General Surgeon</title>
<link rel="stylesheet" href="https://fonts.googleapis.com/css2?family=Montserrat:wght@400;500;600;700&family=Caveat:wght@400;500&display=swap">
<style>
:root{
  --blue:#0a8fd6;
  --blue-deep:#0569b0;
  --blue-bright:#1aa6e6;
  --ink:#1d1d1f;
  --text:#333;
  --line:#d7d7d7;
  --pale:#eef4fa;
  --white:#fff;
}
*{margin:0;padding:0;box-sizing:border-box}
html,body{width:1200px;height:3974px;overflow:hidden}
body{position:relative;font-family:'Montserrat',sans-serif;color:var(--text);background:var(--white)}
.abs{position:absolute}
a{text-decoration:none;color:inherit}

/* header */
.site-header{position:absolute;left:0;top:0;width:1200px;height:111px;background:var(--white)}
.brand{position:absolute;left:113px;top:30px}
.brand-name{font-weight:700;font-size:30px;color:var(--blue);letter-spacing:.5px;line-height:1}
.brand-role{font-family:'Caveat',cursive;font-size:22px;color:#444;line-height:1;margin-top:2px}
.nav a{position:absolute;top:48px;font-size:13px;font-weight:600;color:#333}
.nav .btn-contact{top:35px;left:978px;width:108px;height:42px;border-radius:21px;background:linear-gradient(90deg,var(--blue-bright),var(--blue-deep));color:#fff;display:flex;align-items:center;justify-content:center}

/* hero */
.hero{position:absolute;left:0;top:111px;width:1200px;height:600px;background:linear-gradient(100deg,#1aa3e3 0%,#0b86cf 55%,#0567ad 100%);overflow:hidden}
.hero-title{position:absolute;left:123px;top:176px;font-size:46px;font-weight:700;color:#fff;letter-spacing:.5px}
.hero-role{position:absolute;left:125px;top:232px;font-family:'Caveat',cursive;font-size:32px;color:#fff}
.hero-text{position:absolute;left:128px;top:284px;font-size:14.5px;line-height:21px;color:#fff;width:420px}
.btn-outline{position:absolute;display:flex;align-items:center;justify-content:center;border:2px solid #fff;border-radius:22px;color:#fff;font-weight:700;font-size:15px}
.portrait{position:absolute;left:740px;top:31px;width:355px;height:560px;border-radius:160px 160px 0 0;background:linear-gradient(180deg,#2d3540,#141a22)}

/* headings */
.section-title{position:absolute;font-weight:700;color:var(--ink);font-size:31px;letter-spacing:.3px}
.copy{position:absolute;font-size:15px;line-height:23px;color:#333}

/* services */
.service-card{position:absolute;top:862px;width:297px;height:355px;border:1.5px solid var(--line);text-align:center}
.service-icon{position:absolute;left:82px;top:36px;width:132px;height:132px;border-radius:50%;background:linear-gradient(135deg,var(--blue-bright),var(--blue-deep))}
.service-icon svg{position:absolute;left:36px;top:36px}
.service-name{position:absolute;left:0;top:188px;width:100%;font-size:19px;font-weight:600;color:var(--ink)}
.service-text{position:absolute;left:24px;top:225px;width:249px;font-size:15px;line-height:23px;color:#333}

/* offices */
.office-photo{position:absolute;background:linear-gradient(160deg,#8fbde6,#4a6680 60%,#3a3f46)}

/* booking band */
.booking-band{position:absolute;left:0;top:1957px;width:1200px;height:349px;background:radial-gradient(circle at 65% 30%,#2a9ee2 0%,#0b7fcb 45%,#045aa3 100%)}

/* 3D */
.surgery-3d{position:absolute;left:0;top:2306px;width:1200px;height:594px;background:var(--pale)}
.video{position:absolute;border-radius:8px;overflow:hidden}
.play{position:absolute;width:62px;height:62px;border-radius:50%;background:var(--blue)}
.play::after{content:"";position:absolute;left:25px;top:19px;border-left:17px solid #fff;border-top:12px solid transparent;border-bottom:12px solid transparent}
.btn-fill{position:absolute;display:flex;align-items:center;justify-content:center;border-radius:22px;background:linear-gradient(90deg,var(--blue-bright),var(--blue-deep));color:#fff;font-weight:700;font-size:15px}

/* footer */
.footer-item{position:absolute;top:3690px;color:#fff;font-size:15px;line-height:19px;white-space:nowrap}
.footer-icon{position:absolute;top:3685px;width:40px;height:40px;border:2px solid #fff;border-radius:50%}
.footer-icon svg{position:absolute;left:9px;top:9px}
.footer-nav a{position:absolute;top:3825px;color:#fff;font-size:13px;font-weight:700}
.copyright{position:absolute;left:0;top:3882px;width:1200px;text-align:center;color:#fff;font-size:15px}
</style>
</head>
<body>

<header class="site-header">
  <div class="brand">
    <div class="brand-name">DR K.L. FENWICK</div>
    <div class="brand-role">Consultant General Surgeon</div>
  </div>
  <nav class="nav">
    <a style="left:424px">HOME</a>
    <a style="left:507px">ABOUT</a>
    <a style="left:596px">SERVICES</a>
    <a style="left:708px">PROCEDURES</a>
    <a style="left:847px">SURGERY IN 3D</a>
    <a class="btn-contact">CONTACT</a>
  </nav>
</header>

<section class="hero">
  <svg class="abs" style="left:0;top:0" width="1200" height="600">
    <circle cx="108" cy="20" r="116" fill="#fff" fill-opacity=".18"/>
    <circle cx="0" cy="159" r="62" fill="#fff" fill-opacity=".18"/>
    <circle cx="913" cy="120" r="185" fill="#fff" fill-opacity=".22"/>
  </svg>
  <div class="portrait" role="img" aria-label="Portrait of the surgeon in a dark suit"></div>
  <h1 class="hero-title">DR K.L. FENWICK</h1>
  <div class="hero-role">Consultant General Surgeon</div>
  <p class="hero-text">Lorem ipsum dolor sit amet, consectetur adipiscing eli sed do eiusmod tempor incididunt ut labores.</p>
  <a class="btn-outline" style="left:127px;top:352px;width:259px;height:41px">BOOK AN APPOINTMENT</a>
  <svg class="abs" style="left:0;top:0" width="1200" height="600">
    <path d="M0 560 C140 510 260 490 401 495 C620 505 820 600 1000 591 C1100 586 1160 560 1200 545 L1200 600 L0 600 Z" fill="#fff"/>
  </svg>
</section>

<h2 class="section-title" style="left:0;width:1200px;text-align:center;top:730px">MY SURGICAL SERVICES</h2>
<p class="copy" style="left:0;width:1200px;text-align:center;top:786px">Lorem ipsum dolor sit amet, consectetur adipiscing elit, sed do eiusmod<br>tempor incididunt ut labore et dolore magna aliqua.</p>

<div class="service-card" style="left:126px">
  <div class="service-icon"><svg width="60" height="60" viewBox="0 0 60 60" fill="none" stroke="#fff" stroke-width="2.5" stroke-linejoin="round"><rect x="4" y="6" width="30" height="20" rx="4"/><path d="M12 26 L10 33 L18 26"/><rect x="22" y="20" width="32" height="22" rx="4"/><path d="M44 42 L46 50 L38 42"/><path d="M28 28h20M28 33h20M28 38h14"/></svg></div>
  <div class="service-name">Service Name</div>
  <p class="service-text">Lorem ipsum dolor sit amet, consectetur adipiscing elit, sed do eiusmod tempor incididunt ut labore et dolore magna .</p>
</div>
<div class="service-card" style="left:452px">
  <div class="service-icon"><svg width="60" height="60" viewBox="0 0 60 60" fill="none" stroke="#fff" stroke-width="2.5" stroke-linecap="round"><path d="M48 6 L14 40 L20 46 L54 12"/><path d="M10 44 L4 54 L16 50"/><path d="M30 38 C34 36 42 38 46 44"/></svg></div>
  <div class="service-name">Service Name</div>
  <p class="service-text">Lorem ipsum dolor sit amet, consectetur adipiscing elit, sed do eiusmod tempor incididunt ut labore et dolore magna .</p>
</div>
<div class="service-card" style="left:777px">
  <div class="service-icon"><svg width="60" height="60" viewBox="0 0 60 60" fill="none" stroke="#fff" stroke-width="2.5" stroke-linejoin="round"><path d="M30 52 C10 38 6 28 8 20 C10 10 24 8 30 18 C36 8 50 10 52 20 C54 28 50 38 30 52Z"/><path d="M2 30h16l4-8 6 16 5-12 3 4h22"/></svg></div>
  <div class="service-name">Service Name</div>
  <p class="service-text">Lorem ipsum dolor sit amet, consectetur adipiscing elit, sed do eiusmod tempor incididunt ut labore et dolore magna .</p>
</div>

<h2 class="section-title" style="left:125px;top:1467px">OFFICES</h2>
<p class="copy" style="left:126px;top:1527px;width:312px">Lorem ipsum dolor sit amet, consectetur adipiscing elit, sed do eiusmod tempor incididunt ut labore et dolore magna aliqua. Ut enim ad minim veniam, quis nostrud exercitation ullamco laboris nisi ut aliquip ex ea commodo consequat. Duis aute irure dolor in reprehenderit in voluptate velit esse cillu</p>
<div class="office-photo" style="left:518px;top:1370px;width:300px;height:456px" role="img" aria-label="Modern glass office building"></div>
<div class="office-photo" style="left:834px;top:1370px;width:238px;height:142px" role="img" aria-label="Office building facade"></div>
<div class="office-photo" style="left:834px;top:1529px;width:238px;height:140px;background:linear-gradient(160deg,#3f78c8,#5a6068)" role="img" aria-label="Office building against blue sky"></div>
<div class="office-photo" style="left:834px;top:1686px;width:238px;height:140px;background:linear-gradient(180deg,#9cc2e8,#e4e8ec 60%,#8a8e92)" role="img" aria-label="Low white medical building"></div>

<section class="booking-band">
  <h2 class="section-title" style="left:126px;top:115px;color:#fff;font-size:30px">BOOKING AN APPOINTMENTS</h2>
  <p class="copy" style="left:126px;top:165px;color:#fff;width:580px">Lorem ipsum dolor sit amet, consectetur adipiscing elit, sed do eiusmod tempor incididunt ut labore et dolore magna aliquaipsum suspendisse ultrices gravida. Risus commodo viverra maecenas.</p>
  <a class="btn-outline" style="left:813px;top:161px;width:259px;height:42px">BOOK AN APPOINTMENT</a>
</section>

<section class="surgery-3d">
  <div class="video" style="left:96px;top:100px;width:592px;height:386px;background:linear-gradient(135deg,#4f7fae,#7fa7a4 45%,#3b4f5e)" role="img" aria-label="Video still of a surgical team in theatre"></div>
  <div class="play" style="left:361px;top:262px"></div>
  <h2 class="section-title" style="left:756px;top:153px">SURGERY IN 3D</h2>
  <p class="copy" style="left:756px;top:209px;width:325px">Lorem ipsum dolor sit amet, consectetur adipiscing elit, sed do eiusmod tempor incididunt ut labore et dolore magna aliq uauis ipsum suspendisse ultrices gravida. Risus commodo viverra maecenas acc umsan lacus vel facilisisLorem ipsum do lor sit amet, consectetur.</p>
  <a class="btn-fill" style="left:756px;top:399px;width:154px;height:42px">READ MORE</a>
</section>

<h2 class="section-title" style="left:126px;top:3061px;line-height:39px">SURGICAL<br>PROCEDURES</h2>
<p class="copy" style="left:126px;top:3154px;width:340px">Lorem ipsum dolor sit amet, consectetur adipiscing elit, sed do eiusmod tempor inc ididunt ut labore et dolore magna aliquauis ipsum suspendisse ultrices gravida. Risus commodo viverra maecenas accumsan lac us vel facilisisLorem ipsum dolor sit amet, consectetur adipiscing elit, sed do eiusmod tempor incididunt ut labore.</p>
<a class="btn-fill" style="left:126px;top:3367px;width:156px;height:42px">READ MORE</a>
<div class="video" style="left:494px;top:3052px;width:459px;height:371px;background:linear-gradient(120deg,#3a3a3a,#9a9a9a 50%,#d8d8d8)" role="img" aria-label="Black and white video still of a surgeon"></div>
<div class="play" style="left:520px;top:3335px"></div>
<div class="video" style="left:981px;top:3052px;width:240px;height:371px;border-radius:8px 0 0 8px;background:linear-gradient(160deg,#9fc6e2,#2c5f93 55%,#163a66)" role="img" aria-label="Video still of an operating theatre"></div>
<div class="play" style="left:1006px;top:3335px"></div>

<footer>
  <svg class="abs" style="left:0;top:3500px" width="1200" height="474">
    <defs><linearGradient id="footerGrad" x1="0" y1="0" x2="1" y2="1"><stop offset="0" stop-color="#1aa3e3"/><stop offset="1" stop-color="#0567ad"/></linearGradient></defs>
    <path d="M0 55 C120 90 260 110 420 95 C640 75 820 20 1000 18 C1100 17 1160 22 1200 28 L1200 474 L0 474 Z" fill="url(#footerGrad)"/>
  </svg>
  <div class="footer-icon" style="left:243px"><svg width="18" height="18" viewBox="0 0 18 18" fill="none" stroke="#fff" stroke-width="2"><path d="M9 17 C4 11 3 9 3 7 A6 6 0 0 1 15 7 C15 9 14 11 9 17Z"/><circle cx="9" cy="7" r="2"/></svg></div>
  <div class="footer-item" style="left:299px">Location Name:<br>Loem 412 58 lore519</div>
  <div class="footer-icon" style="left:500px"><svg width="18" height="18" viewBox="0 0 18 18" fill="none" stroke="#fff" stroke-width="2" stroke-linejoin="round"><path d="M3 2h4l2 4-2 2c1 2 3 4 5 5l2-2 4 2v4c-8 0-15-7-15-15Z"/></svg></div>
  <div class="footer-item" style="left:563px">Phone:<br>098 555 01942</div>
  <div class="footer-icon" style="left:747px"><svg width="18" height="18" viewBox="0 0 18 18"><rect x="3" y="5" width="12" height="9" rx="1" fill="#fff"/><path d="M3 6l6 4 6-4" fill="none" stroke="#0a8fd6" stroke-width="1.5"/></svg></div>
  <div class="footer-item" style="left:804px">Email:<br>info@practice.example</div>
  <div class="abs" style="left:140px;top:3774px;width:918px;height:1px;background:rgba(255,255,255,.45)"></div>
  <nav class="footer-nav">
    <a style="left:279px">HOME</a>
    <a style="left:361px">ABOUT</a>
    <a style="left:452px">SERVICES</a>
    <a style="left:565px">PROCEDURES</a>
    <a style="left:703px">SURGERY IN 3D</a>
    <a style="left:851px">CONTACT</a>
  </nav>
  <p class="copyright">Copyright © 2024 All rights are reserved.</p>
</footer>

</body>
</html>
```